Dalton’s Prime Care Vehicle Branding

I am looking to get a half wrap for vehicles to assist in branding for a fire water storm and mold restoration company. I would like to have something similar to the photo loaded to include PWRB Certified Firm Logo and we also use Vans and Trucks...

Target Market(s)

Insurance claims damage from fire water floods and storms and mold....

Requirements
Must have
• The listed logo that I have uploaded. I would also like to have the fact of services provided (see below of services provided)
I would like something for the back of trucks / vans also to be included.

Please list where it looks uniform the following:
- Property Damage Restoration Specialist.
- 24 hr Emergency Service
- Web site: Daltonprimecare.com
- Office line: 730-418-2964

Services Provided to list:
Fire - Water - Mold - Storm
Restoration
Nice to have
• I would like to have some designs that incorporate in the background showing fire, wind / water / possibly if that can fit into what you design and it does not need to overwhelm the design though...
Should not have
• I do not want the logo changed.
I do not want it to be to busy.

```html
<!DOCTYPE html>
<html lang="en">
<head>
<meta charset="utf-8">
<title>Dalton’s Prime Care Vehicle Branding</title>
<link href="https://fonts.googleapis.com/css2?family=Oswald:wght@400;500;700&display=swap" rel="stylesheet">
<style>
  :root {
    --brand-red: #b01f24;
    --deep-red: #9c1a1f;
    --ink: #111111;
    --paper: #ffffff;
    --panel-edge: #d6d6d6;
  }
  html, body { margin: 0; padding: 0; width: 1200px; height: 1200px; overflow: hidden; background: var(--paper); }
  .wrap-sheet { display: block; width: 1200px; height: 1200px; font-family: 'Oswald', sans-serif; }
  .band-top { fill: var(--brand-red); }
  .panel-base { fill: var(--paper); }
  .panel-outline { fill: var(--paper); stroke: var(--panel-edge); stroke-width: 2; }
  .panel-red { fill: var(--brand-red); }
  .stripe { fill: var(--ink); }
  .badge-ring { fill: var(--deep-red); stroke: var(--ink); stroke-width: 9; }
  .badge-arrow { fill: none; stroke: var(--paper); stroke-width: 4; }
  .badge-arrow-head { fill: var(--paper); }
  .badge-text { fill: var(--paper); font-weight: 500; font-size: 18px; text-anchor: middle; }
  .brand-mark { fill: var(--paper); }
  .brand-name { fill: var(--paper); font-weight: 700; font-size: 24px; }
  .brand-phone { fill: var(--paper); font-weight: 500; font-size: 38px; }
  .brand-web { fill: var(--paper); font-weight: 500; font-size: 12px; letter-spacing: 2.2px; }
  .brand-name--small { font-size: 18px; }
  .brand-phone--small { font-size: 28px; }
  .brand-web--small { font-size: 9px; letter-spacing: 1.6px; }
  .headline-red { fill: var(--brand-red); font-weight: 700; font-size: 30px; text-anchor: middle; }
  .headline-ink { fill: var(--ink); font-weight: 400; font-size: 27px; text-anchor: middle; }
  .services-title { fill: var(--brand-red); font-weight: 700; font-size: 19px; text-anchor: middle; }
  .services-list { fill: var(--ink); font-weight: 400; font-size: 18px; text-anchor: middle; }
  .hood-mark { fill: var(--brand-red); }
  .hood-name { fill: var(--brand-red); font-weight: 700; font-size: 30px; }
</style>
</head>
<body>
<svg class="wrap-sheet" viewBox="0 0 1200 1200" xmlns="http://www.w3.org/2000/svg">
  <defs>
    <linearGradient id="fireWater" x1="0" y1="1" x2="1" y2="0">
      <stop offset="0" stop-color="#ffd23a"/>
      <stop offset="0.45" stop-color="#f26a1b"/>
      <stop offset="0.55" stop-color="#5bb4ee"/>
      <stop offset="1" stop-color="#1e6fb8"/>
    </linearGradient>
  </defs>

  <rect class="band-top" x="0" y="0" width="1200" height="440"/>

  <!-- Driver side wrap panel -->
  <g class="side-panel side-panel--driver" transform="translate(100,110)">
    <rect class="panel-base" x="0" y="0" width="1000" height="220" rx="14"/>
    <polygon class="panel-red" points="190,0 700,0 650,220 130,220"/>
    <polygon class="stripe" points="700,0 730,0 680,220 650,220"/>
    <polygon class="stripe" points="748,0 762,0 712,220 698,220"/>
    <g class="illustration" role="img" aria-label="Water droplet over flames illustration">
      <ellipse cx="532" cy="125" rx="50" ry="78" fill="url(#fireWater)"/>
    </g>
    <g class="emergency-badge">
      <circle class="badge-ring" cx="640" cy="110" r="62"/>
      <path class="badge-arrow" d="M602,158 A50,50 0 0 1 660,62"/>
      <polygon class="badge-arrow-head" points="672,60 656,52 658,70"/>
      <text class="badge-text" x="640" y="92">24 hr</text>
      <text class="badge-text" x="640" y="115">Emergency</text>
      <text class="badge-text" x="640" y="138">Service</text>
    </g>
    <g class="brand-block">
      <rect class="brand-mark" x="200" y="62" width="30" height="30"/>
      <text class="brand-name" x="240" y="88">Dalton’s Prime Care</text>
      <text class="brand-phone" x="200" y="150">730-418-2964</text>
      <text class="brand-web" x="201" y="172">Daltonprimecare.com</text>
    </g>
    <text class="headline-red" x="868" y="82">Property Damage</text>
    <text class="headline-ink" x="868" y="116">Restoration Specialist.</text>
  </g>

  <!-- Passenger side wrap panel -->
  <g class="side-panel side-panel--passenger" transform="translate(100,520)">
    <rect class="panel-outline" x="0" y="0" width="1000" height="220" rx="14"/>
    <polygon class="panel-red" points="330,0 870,0 810,220 280,220"/>
    <polygon class="stripe" points="285,0 315,0 265,220 235,220"/>
    <polygon class="stripe" points="262,0 276,0 226,220 212,220"/>
    <g class="illustration" role="img" aria-label="Water droplet over flames illustration">
      <ellipse cx="490" cy="125" rx="52" ry="80" fill="url(#fireWater)"/>
    </g>
    <g class="service-badge">
      <circle class="badge-ring" cx="375" cy="110" r="60"/>
      <path class="badge-arrow" d="M412,156 A48,48 0 0 0 357,64"/>
      <polygon class="badge-arrow-head" points="345,62 361,54 359,72"/>
      <text class="badge-text" x="375" y="117">Restoration</text>
    </g>
    <g class="brand-block">
      <rect class="brand-mark" x="580" y="62" width="30" height="30"/>
      <text class="brand-name" x="620" y="88">Dalton’s Prime Care</text>
      <text class="brand-phone" x="580" y="150">730-418-2964</text>
      <text class="brand-web" x="581" y="172">Daltonprimecare.com</text>
    </g>
    <text class="services-title" x="128" y="80">Services Provided to list:</text>
    <text class="services-list" x="128" y="108">Fire - Water - Mold - Storm</text>
  </g>

  <!-- Hood decal -->
  <g class="hood-panel" transform="translate(100,830)">
    <rect class="panel-outline" x="0" y="0" width="460" height="260" rx="14"/>
    <rect class="hood-mark" x="90" y="112" width="30" height="30"/>
    <text class="hood-name" x="130" y="139">Dalton’s Prime Care</text>
  </g>

  <!-- Tailgate wrap -->
  <g class="tailgate-panel" transform="translate(640,830)">
    <rect class="panel-outline" x="0" y="0" width="460" height="260" rx="14"/>
    <polygon class="panel-red" points="70,0 390,0 360,260 100,260"/>
    <polygon class="stripe" points="40,0 62,0 92,260 70,260"/>
    <polygon class="stripe" points="398,0 420,0 390,260 368,260"/>
    <g class="illustration" role="img" aria-label="Water droplet over flames illustration">
      <ellipse cx="138" cy="165" rx="36" ry="66" fill="url(#fireWater)"/>
    </g>
    <rect class="brand-mark" x="184" y="118" width="20" height="20"/>
    <text class="brand-name brand-name--small" x="212" y="136">Dalton’s Prime Care</text>
    <text class="brand-phone brand-phone--small" x="184" y="180">730-418-2964</text>
    <text class="brand-web brand-web--small" x="185" y="197">Daltonprimecare.com</text>
  </g>
</svg>
</body>
</html>
```